Velvet Fern Beauty Bar Business Card

We need a modern, elegant business card design for our new beauty bar located in La Quinta, CA. The card should feel premium yet approachable, reflecting our brand identity: warm, stylish, and confidence-boosting.

Use our existing Velvet Fern Beauty Bar logo (to be provided as vector file).

Colors: Black, White, Blush / Nude accents, and Gold (metallic or foil effect if possible).

Typography: Clean sans-serif for clarity, with optional elegant script accent.
Design Style

Minimalist and modern with plenty of white space.

Premium look with a beauty/lifestyle feel (not overly corporate).

Option to explore vertical or horizontal orientation.

Rounded corners welcome, but not required.

Additional Notes

Design should print well in both matte and glossy finishes.

Please present mockups with both light and dark backgrounds.

Keep overall feel sleek, feminine, and high-end while still being approachable.

```html
<!DOCTYPE html>
<html lang="en">
<head>
<meta charset="utf-8">
<title>Velvet Fern Beauty Bar – Business Card</title>
<link href="https://fonts.googleapis.com/css2?family=Montserrat:wght@400;500;700&display=swap" rel="stylesheet">
<style>
  :root {
    --backdrop: #1b1b1b;
    --card: #141414;
    --card-back-a: #161616;
    --card-back-b: #242424;
    --gold: #d9b234;
    --gold-light: #f2d572;
    --white: #f2f2f2;
    --silver: #cfcfcf;
  }
  * { margin: 0; padding: 0; box-sizing: border-box; }
  html, body {
    width: 1200px; height: 1059px; overflow: hidden;
    background: var(--backdrop);
    font-family: "Montserrat", sans-serif;
  }
  .card {
    position: absolute;
    left: 254px;
    width: 693px;
    height: 395px;
    box-shadow: 0 8px 24px rgba(0,0,0,.6);
  }
  .card-front { top: 89px; background: var(--card); }
  .card-back {
    top: 545px;
    background: linear-gradient(135deg, var(--card-back-a) 0%, var(--card-back-a) 35%, var(--card-back-b) 60%, var(--card-back-a) 100%);
    display: flex; align-items: center; justify-content: center;
  }
  .brand-name {
    position: absolute;
    left: 28px; top: 40px;
    color: var(--gold);
    font-weight: 500;
    font-size: 38px;
    line-height: 1.1;
    letter-spacing: .5px;
  }
  .brand-name-back {
    position: static;
    color: var(--silver);
    font-size: 52px;
    text-align: center;
  }
  .holder {
    position: absolute;
    right: 27px; top: 30px;
    text-align: right;
    padding-right: 22px;
  }
  .holder-name {
    color: var(--gold);
    font-weight: 700;
    font-size: 29px;
    line-height: 1.1;
  }
  .holder-role {
    color: var(--white);
    font-size: 17px;
    letter-spacing: .6px;
    margin-top: 2px;
  }
  .holder-bar {
    position: absolute;
    right: 0; top: 3px;
    width: 15px; height: 52px;
    background: linear-gradient(180deg, var(--gold-light), var(--gold));
  }
  .address {
    position: absolute;
    left: 24px; top: 207px;
    color: var(--white);
    font-size: 17px;
    line-height: 27px;
    letter-spacing: .6px;
  }
  .contacts {
    position: absolute;
    left: 24px; top: 291px;
    list-style: none;
    color: var(--white);
    font-size: 17px;
    letter-spacing: .6px;
  }
  .contacts li { display: flex; align-items: center; height: 27px; }
  .contacts svg { width: 15px; height: 15px; margin-right: 9px; fill: var(--gold); }
</style>
</head>
<body>
  <section class="card card-front">
    <div class="brand-name">Velvet Fern<br>Beauty Bar</div>

    <div class="holder">
      <div class="holder-name">Daniel Whitford</div>
      <div class="holder-role">Managing Director</div>
      <span class="holder-bar"></span>
    </div>

    <address class="address" style="font-style:normal">
      Your address, City<br>State, Zip 1234
    </address>

    <ul class="contacts">
      <li>
        <svg viewBox="0 0 16 16" aria-hidden="true"><path d="M1 6c0-2 3-3 7-3s7 1 7 3v1h-3V5.5C11 5 9.5 5 8 5s-3 0-4 .5V7H1zM3 8h10l1 6H2z"/></svg>
        123 456 789
      </li>
      <li>
        <svg viewBox="0 0 16 16" aria-hidden="true"><path d="M1 3h14v10H1zM2 4l6 5 6-5"/></svg>
        info@velvetfern.com
      </li>
      <li>
        <svg viewBox="0 0 16 16" aria-hidden="true"><circle cx="8" cy="8" r="7"/></svg>
        www.velvetfern.com
      </li>
    </ul>
  </section>

  <section class="card card-back">
    <div class="brand-name brand-name-back">Velvet Fern Beauty Bar</div>
  </section>
</body>
</html>
```